Website for my law practice

I am a solo practitioner, who specializes in family law and estate planning in Massachusetts. I need to re-do my website, as it is outdated. I like the idea of a nontraditional law firm website. My website address is: rosalindhartwelllaw.com. I would like to retain my logo in the green color, as part of the new website. I have uploaded my logo below.
Updates

My hourly rate has changed from what is listed on my current website. My new hourly rate is $385.00. Please use this hourly rate when creating the website.

Good morning,

I have reviewed the designs submitted so far. I am happy that the "rh" logo in the green color is part of each of the designs submitted. I am also happy that the standard items seen in law firm websites, such as the scales of justice, etc. were not incorporated. Although the green logo is great, I do not think rest of the website has to have the same green color throughout. Additionally, I was hoping for something more creative, to make the website standout and not the stock web designs you see everyday. Please incorporate more unique images if you can. For example of what I mean, please look at this website: https://www.lorettafinchlaw.com

Coding

```html
<!DOCTYPE html>
<html lang="en">
<head>
<meta charset="utf-8">
<title>Rosalind Hartwell – Attorney at Law</title>
<link href="https://fonts.googleapis.com/css2?family=Gilda+Display&family=Poppins:wght@300;400;500;600&display=swap" rel="stylesheet">
<style>
:root{
  --green:#2f8c2c;
  --ink:#1f2623;
  --slate:#2e3a40;
  --clay:#b5785a;
  --clay-soft:#e8d6c8;
  --sand:#f3ebe2;
  --cream:#fcf7f2;
  --card:#f6f1ea;
  --text:#3a3a3a;
  --footer:#1d2124;
  --white:#ffffff;
  --gold:#c99a2e;
}
*{margin:0;padding:0;box-sizing:border-box}
html,body{width:1200px;height:3950px;overflow:hidden}
body{background:var(--cream);font-family:"Poppins",sans-serif;color:var(--text);position:relative}
.abs{position:absolute}
.serif{font-family:"Gilda Display",serif;font-weight:400}
p{font-size:11.5px;line-height:1.5}
.btn{position:absolute;background:var(--ink);color:var(--white);border-radius:6px;font-size:12px;display:flex;align-items:center;justify-content:center;text-decoration:none;box-shadow:0 3px 8px rgba(0,0,0,.15)}
.btn--clay{background:var(--clay)}
.photo{position:absolute;overflow:hidden}

/* header */
.site-header{position:absolute;left:0;top:0;width:1200px;height:122px;background:var(--cream)}
.brand{position:absolute;display:flex;align-items:center;gap:12px}
.brand-mark{width:40px;height:40px;border-radius:50%;border:5px solid var(--green);flex:none}
.brand-name{color:var(--green);font-weight:600;font-size:12px;line-height:1.3}
.nav a{position:absolute;top:56px;font-size:13px;color:var(--ink);text-decoration:none}
.nav a.active{color:var(--clay);font-weight:500}
.nav a.active::after{content:"";position:absolute;left:0;right:0;bottom:-8px;height:2px;background:var(--clay)}

/* hero */
.hero{left:0;top:122px;width:1200px;height:562px;
  background:
    radial-gradient(ellipse 380px 420px at 820px 230px,rgba(150,120,90,.55),transparent 70%),
    radial-gradient(ellipse 500px 160px at 640px 520px,rgba(120,70,40,.7),transparent 70%),
    linear-gradient(180deg,#44525f 0%,#36434f 58%,#5b3d27 84%,#3b2416 100%)}
.hero::before{content:"";position:absolute;inset:0;background:linear-gradient(90deg,rgba(20,28,34,.55) 0%,rgba(20,28,34,0) 55%)}
.hero-text{left:97px;top:326px;color:var(--white)}
.hero-dots span{position:absolute;left:1152px;width:6px;height:6px;border-radius:50%;background:#dcdcdc}
.down{left:560px;top:644px;width:80px;height:80px;border-radius:50%;background:var(--cream)}

/* expertise */
.expert-band{left:0;top:1334px;width:600px;height:567px;background:var(--slate)}
.expert-band::after{content:"";position:absolute;right:0;top:0;width:6px;height:100%;background:var(--clay)}
.expert-list li{position:absolute;list-style:none;font-size:15px;color:var(--ink);padding-left:36px;line-height:1.45}

/* testimonials */
.testimonial{position:absolute;top:2663px;width:564px;height:184px}
.t-card{position:absolute;left:46px;top:0;width:518px;height:184px;background:var(--white);border-radius:10px;box-shadow:0 6px 18px rgba(60,40,20,.06)}
.t-photo{position:absolute;left:10px;top:-12px;width:210px;height:210px;border-radius:50%;
  background:radial-gradient(circle at 40% 35%,#e6d3bd,#c2a07f 55%,#7f5c45)}

/* contact */
.field{position:absolute;background:var(--white);border-radius:8px;font-size:11px;color:#555;padding:14px 18px;border:1px solid #efe6dc}

/* footer */
.footer{left:0;top:3507px;width:1200px;height:443px;background:var(--footer);color:var(--white)}
.footer h4{font-size:12px;font-weight:600}
.footer li{list-style:none;font-size:12px;line-height:1.6}
.social span{display:inline-block;width:28px;height:28px;border-radius:50%;border:1.5px solid var(--white);margin-right:8px}
</style>
</head>
<body>

<header class="site-header">
  <div class="brand" style="left:84px;top:40px">
    <span class="brand-mark"></span>
    <span class="brand-name">Rosalind Hartwell<br>Attorney at Law</span>
  </div>
  <nav class="nav">
    <a class="active" href="#" style="left:437px">Home</a>
    <a href="#" style="left:502px">About us</a>
    <a href="#" style="left:584px">Family Law</a>
    <a href="#" style="left:679px">EstatePlanning</a>
    <a href="#" style="left:798px">FAQ</a>
    <a href="#" style="left:852px">Contact us</a>
  </nav>
  <a class="btn" href="#" style="left:980px;top:44px;width:145px;height:37px">Free Consultation</a>
</header>

<section class="hero abs" role="img" aria-label="Bronze statue holding scales beside a gavel and an open book on a wooden desk"></section>
<div class="hero-text abs">
  <div style="font-size:19px;letter-spacing:2px">Welcome to</div>
  <div class="serif" style="font-size:47px;line-height:1.15;letter-spacing:1px">Rosalind Hartwell</div>
  <div style="font-size:20px;letter-spacing:10px;margin-top:2px">Attorney at Law</div>
</div>
<a class="btn btn--clay" href="#" style="left:97px;top:454px;width:145px;height:40px">Read More</a>
<div class="hero-dots">
  <span style="top:354px"></span>
  <span style="top:378px"></span>
  <span style="top:400px;left:1145px;width:20px;height:20px;background:var(--clay);color:#fff;font-size:8px;display:flex;align-items:center;justify-content:center">03</span>
  <span style="top:446px"></span>
</div>
<div class="down abs"></div>
<svg class="abs" style="left:590px;top:672px" width="20" height="26" viewBox="0 0 20 26"><path d="M10 2v20M3 15l7 7 7-7" fill="none" stroke="#b5785a" stroke-width="2"/></svg>

<!-- about -->
<svg class="abs" style="left:170px;top:765px" width="450" height="450" viewBox="0 0 450 450">
  <circle cx="225" cy="225" r="212" fill="none" stroke="#2f8c2c" stroke-width="16" stroke-dasharray="1100 232" transform="rotate(-85 225 225)"/>
</svg>
<div class="photo" style="left:195px;top:788px;width:396px;height:396px;border-radius:50%;background:radial-gradient(circle at 50% 40%,#e7c58a 0%,#c79a5c 35%,transparent 62%),linear-gradient(180deg,#7fa9cc 0%,#a9c0cf 45%,#8a8d6c 100%)" role="img" aria-label="Portrait of Rosalind Hartwell outdoors by the water"></div>
<h2 class="serif abs" style="left:664px;top:808px;font-size:44px;color:var(--green);line-height:1">Rosalind Hartwell</h2>
<div class="abs" style="left:621px;top:866px;width:440px;height:1px;background:#8a8a8a"></div>
<div class="abs" style="left:664px;top:883px;width:405px">
  <p>Rosalind Hartwell is a Solo Practitioner focusing her practice on matters pertaining to family law and estate planning.</p>
  <p style="color:var(--clay);font-weight:600;margin-top:12px">Close, Personal Representation</p>
  <p>When I am retained, my clients are my priority. As a result, I work closely with each one to keep them informed through each step of the legal proceeding. Clients have always expressed to me how frustrating it is when attorneys don't return phone calls. I understand this, as I am often met with the same challenges in the profession. I am proud of my practice and my reputation, and I return calls promptly.</p>
  <p style="margin-top:16px">I try and answer questions in plain and simple language, as well as provide my clients with possible scenarios and options they have.</p>
</div>
<a class="btn" href="#" style="left:665px;top:1119px;width:145px;height:41px">Read More</a>
<svg class="abs" style="left:832px;top:1129px" width="22" height="22" viewBox="0 0 22 22"><circle cx="11" cy="11" r="9.5" fill="none" stroke="#b5785a" stroke-width="1.5"/><path d="M6 11l4 4 7-8" fill="none" stroke="#b5785a" stroke-width="1.8"/></svg>
<div class="abs" style="left:860px;top:1133px;font-size:11.5px;font-weight:600;color:var(--ink)">Free 30-Minute Consultation</div>

<!-- expertise -->
<div class="expert-band abs"></div>
<div class="photo" style="left:600px;top:1334px;width:600px;height:567px;background:radial-gradient(ellipse 260px 220px at 300px 230px,#e8cdb3,transparent 70%),radial-gradient(ellipse 300px 140px at 320px 480px,#8c5f3f,transparent 70%),linear-gradient(135deg,#cfbfae,#efe4d8 45%,#a57d5f)" role="img" aria-label="Parents smiling while drawing with their young daughter at a table"></div>
<div class="abs" style="left:78px;top:1400px;width:597px;height:434px;background:var(--card)"></div>
<div class="abs" style="left:140px;top:1458px;font-size:15px;color:var(--ink)">Case Studies</div>
<h2 class="serif abs" style="left:131px;top:1478px;font-size:46px;color:var(--clay)">Areas of Expertise</h2>
<ul class="expert-list">
  <li style="left:133px;top:1543px">Durable Power of Attorney<br>with Nomination of Guardian</li>
  <li style="left:133px;top:1598px">Memorandum of Remains</li>
  <li style="left:133px;top:1632px">Revocable Living Trust</li>
  <li style="left:133px;top:1671px">Quitclaim Deed</li>
  <li style="left:133px;top:1706px">Health Care Proxy</li>
  <li style="left:400px;top:1545px">Will</li>
  <li style="left:400px;top:1602px">Memorandum of Remains</li>
  <li style="left:400px;top:1635px">Trustee's Certificate</li>
  <li style="left:400px;top:1672px">Irrevocable Living Trust</li>
  <li style="left:400px;top:1707px">Trust Amendments</li>
</ul>
<svg width="0" height="0" style="position:absolute"><defs><g id="tk"><circle cx="11" cy="11" r="9.5" fill="none" stroke="#1f2623" stroke-width="1.5"/><path d="M6 11l4 4 7-8" fill="none" stroke="#1f2623" stroke-width="1.6"/></g></defs></svg>
<svg class="abs" style="left:133px;top:1545px" width="22" height="22"><use href="#tk"/></svg>
<svg class="abs" style="left:133px;top:1600px" width="22" height="22"><use href="#tk"/></svg>
<svg class="abs" style="left:133px;top:1634px" width="22" height="22"><use href="#tk"/></svg>
<svg class="abs" style="left:133px;top:1673px" width="22" height="22"><use href="#tk"/></svg>
<svg class="abs" style="left:133px;top:1708px" width="22" height="22"><use href="#tk"/></svg>
<svg class="abs" style="left:400px;top:1547px" width="22" height="22"><use href="#tk"/></svg>
<svg class="abs" style="left:400px;top:1604px" width="22" height="22"><use href="#tk"/></svg>
<svg class="abs" style="left:400px;top:1637px" width="22" height="22"><use href="#tk"/></svg>
<svg class="abs" style="left:400px;top:1674px" width="22" height="22"><use href="#tk"/></svg>
<svg class="abs" style="left:400px;top:1709px" width="22" height="22"><use href="#tk"/></svg>
<a class="btn" href="#" style="left:132px;top:1754px;width:145px;height:40px">View More</a>
<div class="abs" style="left:312px;top:1746px;width:56px;height:56px;border-radius:50%;background:var(--white);box-shadow:0 3px 10px rgba(0,0,0,.08)"></div>
<svg class="abs" style="left:326px;top:1764px" width="28" height="20" viewBox="0 0 28 20"><path d="M2 10h23M17 3l8 7-8 7" fill="none" stroke="#b5785a" stroke-width="2"/></svg>

<!-- why -->
<div class="abs" style="left:253px;top:2060px;width:358px;height:360px;border-radius:0 0 22px 0;border-right:12px solid var(--clay);border-bottom:12px solid var(--clay)"></div>
<div class="photo" style="left:155px;top:2013px;width:446px;height:394px;border-radius:22px;background:radial-gradient(ellipse 200px 170px at 240px 170px,#e6c9ad,transparent 70%),radial-gradient(ellipse 240px 100px at 230px 360px,#f4f0ea,transparent 70%),linear-gradient(135deg,#c8b7a4,#ece1d4 45%,#9b7457)" role="img" aria-label="Family sitting together at a table while the child draws on paper"></div>
<h2 class="serif abs" style="left:661px;top:2025px;font-size:45px;line-height:1;color:var(--ink)">Why Hiring an<br>Attorney is the Right<br>Choice</h2>
<div class="abs" style="left:666px;top:2171px;width:365px">
  <p>Whether you are creating an estate plan for the first time or updating your existing plan, I strive to make the estate planning process easy to understand, comfortable and comprehensive.</p>
  <p style="margin-top:16px">Throughout the process of drafting an estate plan, additional professionals such as a financial planner, CPA and life insurance agent may become necessary resources in the handling of your assets. If this is necessary, I will advise you accordingly and provide you with a list of knowledgeable professionals to choose from.</p>
</div>
<a class="btn" href="#" style="left:666px;top:2361px;width:145px;height:40px">Read More</a>

<!-- testimonials -->
<h2 class="serif abs" style="left:0;width:1200px;text-align:center;top:2525px;font-size:46px;color:var(--ink)">What Our Clients Say</h2>
<div class="abs" style="left:0;width:1185px;text-align:center;top:2584px;font-size:15px;color:var(--ink)">Testimonials</div>

<div class="testimonial" style="left:66px">
  <div class="t-card"></div>
  <svg class="abs" style="left:-4px;top:-26px" width="238" height="238" viewBox="0 0 238 238"><circle cx="119" cy="119" r="113" fill="none" stroke="#b5785a" stroke-width="8" stroke-dasharray="470 240" transform="rotate(100 119 119)"/></svg>
  <div class="t-photo" role="img" aria-label="Smiling couple looking at papers together"></div>
  <div class="abs serif" style="left:252px;top:16px;font-size:48px;color:var(--clay);line-height:1">“</div>
  <div class="abs" style="left:252px;top:60px;font-size:11.5px;font-weight:600;color:var(--ink)">-Melissa Grant</div>
  <p class="abs" style="left:252px;top:82px;width:235px">Lorem Ipsum is simply dummy text of the printing and typesetting industry has been the industry's standard dummy.</p>
  <div class="abs" style="left:252px;top:136px;font-size:11px;color:var(--gold);letter-spacing:4px">★★★★★</div>
</div>
<div class="testimonial" style="left:602px">
  <div class="t-card"></div>
  <svg class="abs" style="left:-4px;top:-26px" width="238" height="238" viewBox="0 0 238 238"><circle cx="119" cy="119" r="113" fill="none" stroke="#b5785a" stroke-width="8" stroke-dasharray="470 240" transform="rotate(100 119 119)"/></svg>
  <div class="t-photo" role="img" aria-label="Smiling couple looking at papers together"></div>
  <div class="abs serif" style="left:252px;top:16px;font-size:48px;color:var(--clay);line-height:1">“</div>
  <div class="abs" style="left:252px;top:60px;font-size:11.5px;font-weight:600;color:var(--ink)">-Melissa Grant</div>
  <p class="abs" style="left:252px;top:82px;width:235px">Lorem Ipsum is simply dummy text of the printing and typesetting industry has been the industry's standard dummy.</p>
  <div class="abs" style="left:252px;top:136px;font-size:11px;color:var(--gold);letter-spacing:4px">★★★★★</div>
</div>
<div class="abs" style="left:552px;top:2922px;width:36px;height:3px;background:var(--clay)"></div>
<div class="abs" style="left:594px;top:2922px;width:20px;height:3px;background:#bbb"></div>
<div class="abs" style="left:623px;top:2922px;width:20px;height:3px;background:#bbb"></div>

<!-- quick contact -->
<h2 class="serif abs" style="left:110px;top:3030px;font-size:46px;color:var(--ink)">Quick Contact</h2>
<div class="field" style="left:113px;top:3107px;width:234px;height:42px">Name</div>
<div class="field" style="left:359px;top:3107px;width:234px;height:42px">Phone</div>
<div class="field" style="left:113px;top:3166px;width:234px;height:42px">Email</div>
<div class="field" style="left:359px;top:3166px;width:234px;height:42px">Areas of Expertise<span style="position:absolute;right:14px">⌄</span></div>
<div class="field" style="left:113px;top:3225px;width:480px;height:102px">Message</div>
<a class="btn" href="#" style="left:109px;top:3351px;width:145px;height:40px">Submit</a>
<div class="abs" style="left:770px;top:3032px;width:358px;height:338px;background:var(--clay);border-radius:22px"></div>
<div class="photo" style="left:661px;top:3047px;width:450px;height:376px;border-radius:0 0 22px 22px;background:radial-gradient(ellipse 200px 90px at 230px 290px,#b0695a,transparent 70%),radial-gradient(ellipse 260px 120px at 260px 200px,#efe9e0,transparent 70%),linear-gradient(180deg,#d2dce5 0%,#e7e3dd 48%,#9e7a6c 80%,#6b6b68 100%)" role="img" aria-label="Street view of the office building on a corner in spring"></div>

<!-- footer -->
<footer class="footer abs">
  <div class="brand" style="left:152px;top:117px">
    <span class="brand-mark" style="width:46px;height:46px"></span>
    <span class="brand-name">Rosalind Hartwell<br>Attorney at Law</span>
  </div>
  <div class="social abs" style="left:170px;top:217px"><span style="background:var(--clay);border-color:var(--clay)"></span><span></span><span></span><span></span></div>
  <div class="abs" style="left:458px;top:118px">
    <h4>Quick Links</h4>
    <ul style="margin-top:12px">
      <li style="font-weight:600">› Home</li><li>› About us</li><li>› Family Law</li><li>› EstatePlanning</li><li>› FAQ</li><li>› Contact us</li>
    </ul>
  </div>
  <div class="abs" style="left:662px;top:118px;width:280px">
    <h4>Contact Info</h4>
    <svg class="abs" style="left:0;top:33px" width="12" height="14" viewBox="0 0 12 14"><path d="M6 13s5-5 5-8a5 5 0 0 0-10 0c0 3 5 8 5 8z" fill="none" stroke="#fff" stroke-width="1.2"/><circle cx="6" cy="5" r="1.7" fill="none" stroke="#fff" stroke-width="1.2"/></svg>
    <ul class="abs" style="left:24px;top:29px;width:240px"><li style="font-size:11px">742 Linden Row<br>Ashbury, MA 01870</li></ul>
    <svg class="abs" style="left:0;top:82px" width="12" height="12" viewBox="0 0 12 12"><path d="M2 1l2.5 0 1 3-1.5 1a7 7 0 0 0 3 3l1-1.5 3 1V11c-5 0-9-4-9-10z" fill="none" stroke="#fff" stroke-width="1.1"/></svg>
    <ul class="abs" style="left:24px;top:79px"><li style="font-size:11px">978-555-0142<br>978-555-0187</li></ul>
    <svg class="abs" style="left:0;top:135px" width="13" height="10" viewBox="0 0 13 10"><rect x="0.6" y="0.6" width="11.8" height="8.8" fill="none" stroke="#fff" stroke-width="1.1"/><path d="M1 1l5.5 4.5L12 1" fill="none" stroke="#fff" stroke-width="1.1"/></svg>
    <ul class="abs" style="left:24px;top:130px;width:260px"><li style="font-size:11px;text-decoration:underline">rosalind@rosalindhartwelllaw.com</li></ul>
  </div>
  <div class="abs" style="left:970px;top:107px;width:140px;height:150px;background:var(--sand);border:4px solid var(--white)" role="img" aria-label="Client satisfaction award badge"></div>
  <div class="abs" style="left:0;top:371px;width:1200px;height:72px;background:var(--cream);font-size:11px;color:var(--ink);text-align:center;line-height:72px">Copyright ©2025, Rosalind Hartwell, All Rights Reserved.</div>
</footer>

</body>
</html>
```